Marrow Creek 381 Wine Label

Marrow Creek 381 Wine bottle label-
Pinot Noir, Chardonnay. Premium label.
Startup vineyard, Cool climate, Tasmania Australia.
Hills and Valley area, South East location
Needs to be a front and rear label as there are label requirements in Australia. Rear lable
is mearly to talk about the wine and have required information as per the examples uploaded

```html
<!DOCTYPE html>
<html lang="en">
<head>
<meta charset="utf-8">
<title>Marrow Creek 381 — Front Label</title>
<link href="https://fonts.googleapis.com/css2?family=EB+Garamond:wght@400;500&display=swap" rel="stylesheet">
<style>
  :root {
    --page: #ffffff;
    --cream: #f3efdf;
    --slate: #2a2d34;
    --gold: #b8874a;
    --ink: #3b3732;
    --rule: #8f8a80;
  }
  * { margin: 0; padding: 0; box-sizing: border-box; }
  html, body {
    width: 1200px;
    height: 1200px;
    overflow: hidden;
    background: var(--page);
    font-family: "EB Garamond", Georgia, serif;
  }
  .label {
    position: absolute;
    left: 220px;
    top: 162px;
    width: 760px;
    height: 876px;
    background: var(--cream);
    border-radius: 12px;
    overflow: hidden;
  }
  .origin {
    position: absolute;
    top: 48px;
    width: 100%;
    text-align: center;
    font-size: 16px;
    letter-spacing: 2.4px;
    color: var(--ink);
  }
  .identity {
    position: absolute;
    top: 194px;
    left: 0;
    width: 100%;
    display: flex;
    align-items: stretch;
  }
  .brand-name {
    width: 320px;
    padding-right: 14px;
    padding-top: 12px;
    text-align: right;
    color: var(--gold);
    font-weight: 500;
    font-size: 30px;
    line-height: 1.05;
    letter-spacing: 0.5px;
  }
  .brand-name span { display: block; }
  .brand-name .number { font-size: 62px; line-height: 1; }
  .divider {
    width: 1px;
    background: var(--rule);
  }
  .wine-details {
    padding-left: 12px;
    padding-top: 2px;
    padding-bottom: 8px;
    color: var(--ink);
  }
  .varietal { font-size: 33px; line-height: 1.2; }
  .vintage { font-size: 33px; line-height: 1.25; }
  .spec { font-size: 16px; line-height: 1.35; }
  .terrain {
    position: absolute;
    left: 0;
    top: 432px;
    width: 760px;
    height: 444px;
  }
  .terrain-signature {
    position: absolute;
    left: 0;
    top: 698px;
    width: 760px;
    text-align: center;
    color: var(--gold);
    font-size: 21px;
    transform: translateX(-8px);
  }
</style>
</head>
<body>
  <div class="label">
    <p class="origin">WINE OF TASMANIA, AUSTRALIA</p>

    <div class="identity">
      <div class="brand-name">
        <span>MARROW CREEK</span>
        <span class="number">381</span>
      </div>
      <div class="divider"></div>
      <div class="wine-details">
        <p class="varietal">Pinot Noir &amp; Chardonnay</p>
        <p class="vintage">2025</p>
        <p class="spec">750 ml</p>
        <p class="spec">12% Vol.</p>
      </div>
    </div>

    <svg class="terrain" viewBox="0 0 760 444" role="img" aria-label="Topographic contour map of the vineyard hills on a dark slate band">
      <defs>
        <linearGradient id="terrainShade" x1="0" y1="0" x2="1" y2="1">
          <stop offset="0" stop-color="#2c2f36"/>
          <stop offset="1" stop-color="#272a31"/>
        </linearGradient>
      </defs>
      <path fill="url(#terrainShade)" d="M0 12 L20 9 L38 12 L55 7 L74 11 L92 8 L110 12 L128 6 L146 10 L165 7 L184 11 L203 5 L222 10 L240 7 L258 12 L277 6 L296 10 L315 8 L334 12 L352 5 L371 9 L390 7 L409 11 L428 6 L447 10 L466 8 L485 12 L504 5 L523 9 L542 7 L561 11 L580 6 L599 10 L618 8 L637 11 L656 5 L675 9 L694 7 L713 11 L732 6 L760 9 L760 444 L0 444 Z"/>
    </svg>

    <p class="terrain-signature">Marrow Creek 381</p>
  </div>
</body>
</html>
```